A 24' X 36" SIGN TO ANNOUNCE "ORDER YOUR TURKEY EARLY"

MUST INCLUDE OUR LOGO(PROVIDED), black background, TEXT to include
all natural
farm raised
no hormones

The sign needs to be designed for vertical(portrait) viewing. The logo needs to be smaller and emphasis on TURKEY

Farm

```html
<!DOCTYPE html>
<html lang="en">
<head>
<meta charset="utf-8">
<title>Order Your Turkey Early</title>
<link rel="stylesheet" href="https://fonts.googleapis.com/css2?family=Tinos&display=swap">
<style>
  :root {
    --backdrop: #e9eaec;
    --sign-black: #000000;
    --gold: #f3d21c;
    --white: #ffffff;
  }
  * { margin: 0; padding: 0; box-sizing: border-box; }
  html, body {
    width: 1200px;
    height: 1000px;
    overflow: hidden;
    background: var(--backdrop);
  }
  .sign {
    position: absolute;
    left: 300px;
    top: 50px;
    width: 600px;
    height: 900px;
    background: var(--sign-black);
    font-family: "Tinos", "Times New Roman", serif;
    font-weight: 400;
    text-align: center;
    box-shadow: 0 6px 18px rgba(0,0,0,0.25);
  }
  .sign-border {
    position: absolute;
    inset: 16px 18px;
    border: 3px solid var(--gold);
  }
  .headline {
    position: absolute;
    left: 0;
    right: 0;
    top: 52px;
    font-weight: 400;
    line-height: 1;
  }
  .headline-small {
    display: block;
    color: var(--white);
    font-size: 36px;
    letter-spacing: 0.5px;
  }
  .headline-turkey {
    display: block;
    color: var(--gold);
    font-size: 88px;
    letter-spacing: 1px;
    margin: -2px 0 -4px;
  }
  .dotted-rule {
    position: absolute;
    left: 120px;
    width: 360px;
    border-top: 3px dotted var(--gold);
  }
  .rule-top { top: 245px; }
  .rule-bottom { top: 726px; }
  .feature {
    position: absolute;
    left: 95px;
    width: 410px;
    height: 88px;
    border: 1.5px solid var(--gold);
    display: flex;
    align-items: center;
    justify-content: center;
  }
  .feature-label {
    color: var(--gold);
    font-size: 42px;
    letter-spacing: 0.5px;
    line-height: 1;
  }
  .feature-natural { top: 290px; }
  .feature-farm { top: 437px; }
  .feature-hormones { top: 584px; }
  .market-name {
    position: absolute;
    left: 0;
    right: 0;
    top: 790px;
    color: var(--gold);
    font-size: 22px;
    letter-spacing: 2px;
  }
</style>
</head>
<body>
  <main class="sign">
    <div class="sign-border"></div>

    <h1 class="headline">
      <span class="headline-small">ORDER YOUR</span>
      <span class="headline-turkey">TURKEY</span>
      <span class="headline-small">EARLY</span>
    </h1>

    <div class="dotted-rule rule-top"></div>

    <div class="feature feature-natural">
      <p class="feature-label">ALL NATURAL</p>
    </div>

    <div class="feature feature-farm">
      <p class="feature-label">FARM RAISED</p>
    </div>

    <div class="feature feature-hormones">
      <p class="feature-label">NO HORMONES</p>
    </div>

    <div class="dotted-rule rule-bottom"></div>

    <p class="market-name">HOLLOWBROOK MARKET</p>
  </main>
</body>
</html>
```